Roofing web site brel roofing

Look at some of our competitors web page we like something similar with NYC roofing
https://www.dovantileworks.example/
Maybe a skyline picture of nyc at the home page with a picture of flat roofing installation

Target Market(s)

Commercial and residential flat roofs

Industry/Entity Type

Flat Roofing industry

Coding

Coded - Design and coding required

Number of Pages Required

2 page

Font styles to use
Decorative
Script

Colors

Designer to choose colors to be used in the design.

Requirements
Must have
• At BREL Roofing, we are a trusted and reputable roofing company specializing in new construction flat roof installation and repair. With years of experience in the industry, we take pride in providing exceptional roofing solutions to our valued clients. Our team of highly skilled and dedicated roofing professionals understands the unique challenges and requirements of new construction projects. We work closely with builders, contractors, and architects to design and install flat roofs that meet the specific needs of each project. From commercial buildings to residential complexes, we have the expertise to deliver reliable and durable roofing solutions. When it comes to flat roof repairs, we are your go-to experts. Our experienced technicians conduct thorough inspections to identify the root cause of any issues your roof may be experiencing. We utilize the latest industry techniques and high-quality materials to efficiently repair your flat roof, ensuring its integrity and longevity. At BREL Roofing, we prioritize customer satisfaction above all else. We believe in building strong relationships with our clients by providing exceptional craftsmanship and outstanding customer service. Our team is dedicated to delivering projects on time, within budget, and to the highest standards of quality. We understand that a well-maintained roof is essential for protecting your property and ensuring the safety of its occupants. That's why we use only the best materials and employ skilled professionals who are trained in the latest roofing practices. Our commitment to excellence is evident in every project we undertake. As a fully licensed and insured roofing company, we prioritize safety and adhere to industry regulations and best practices. We take every precaution to create a safe working environment for our team and minimize any disruptions to your daily routine. When you choose BREL Roofing, you can trust that you are working with a reliable and reputable company that will deliver exceptional results. We are committed to exceeding your expectations and providing you with a roof that is built to last. Contact us today for all your new construction flat roof installation and repair needs.
Nice to have
• NYC skyline background with commercial roofing pictures of torching roofing

```html
<!DOCTYPE html>
<html lang="en">
<head>
<meta charset="utf-8">
<title>BREL Roofing – Flat Roof Installation &amp; Repair</title>
<link href="https://fonts.googleapis.com/css2?family=Poppins:wght@400;500;600;700;800&display=swap" rel="stylesheet">
<style>
:root{
  --orange:#f26522;
  --orange-dark:#d9531a;
  --ink:#1d1d1f;
  --text:#5d5d63;
  --muted:#8a8a90;
  --blush:#fdf0ec;
  --white:#ffffff;
  --night:#16181c;
  --night-2:#22252b;
  --sky-1:#2b3340;
  --sky-2:#6c7480;
}
*{box-sizing:border-box;margin:0;padding:0}
html,body{width:1200px;height:4144px;overflow:hidden}
body{font-family:"Poppins",sans-serif;color:var(--ink);background:var(--white);position:relative}
a{color:inherit;text-decoration:none}
.btn{display:inline-flex;align-items:center;justify-content:center;background:var(--orange);color:var(--white);font-weight:600;font-size:16px;letter-spacing:.5px;text-transform:uppercase;height:52px;padding:0 34px}

/* header */
.site-header{position:absolute;top:0;left:0;width:1200px;height:112px;background:var(--white);z-index:5}
.brand{position:absolute;left:0;top:0;width:240px;height:112px;background:var(--orange);color:var(--white);font-weight:800;font-size:30px;line-height:1.05;display:flex;flex-direction:column;justify-content:center;padding-left:24px;text-transform:uppercase}
.topbar{position:absolute;left:280px;top:0;right:0;height:44px;display:flex;align-items:center;gap:36px;font-size:15px;color:var(--ink);border-bottom:1px solid #eee}
.topbar span{display:flex;align-items:center;gap:10px}
.topbar .dot{width:22px;height:22px;border-radius:50%;background:var(--orange);display:inline-flex;align-items:center;justify-content:center}
.socials{margin-left:auto;margin-right:30px;display:flex;gap:14px}
.socials i{width:14px;height:14px;border-radius:50%;background:var(--orange);display:block}
.main-nav{position:absolute;left:296px;top:44px;height:68px;display:flex;align-items:center;gap:42px;font-weight:500;font-size:17px;text-transform:uppercase}
.header-cta{position:absolute;right:0;top:48px;width:220px;height:64px;background:var(--orange);color:var(--white);font-weight:600;font-size:16px;display:flex;align-items:center;justify-content:center}

/* hero */
.hero{position:absolute;top:0;left:0;width:1200px;height:660px;background:linear-gradient(180deg,#3a414c 0%,#56606c 45%,#2a2f37 100%)}
.hero::after{content:"";position:absolute;inset:0;background:linear-gradient(90deg,rgba(10,12,16,.7) 0%,rgba(10,12,16,.25) 70%)}
.hero-copy{position:absolute;left:120px;top:180px;z-index:2;color:var(--white);width:640px}
.hero-copy h1{font-size:64px;font-weight:700;line-height:1.12}
.hero-copy h1 em{font-style:normal;color:var(--orange)}
.hero-copy p{font-size:19px;line-height:1.5;margin:22px 0 36px;width:560px}

/* feature cards */
.features{position:absolute;top:636px;left:120px;width:960px;display:flex;justify-content:space-between;z-index:3}
.feature{width:296px;height:296px;background:var(--white);box-shadow:0 14px 40px rgba(0,0,0,.12);text-align:center;padding:34px 26px 0;position:relative}
.feature .icon{width:96px;height:96px;border-radius:50%;background:var(--blush);margin:0 auto 18px;display:flex;align-items:center;justify-content:center}
.feature h3{font-size:24px;font-weight:700}
.feature p{font-size:13px;color:var(--muted);line-height:1.5;margin-top:8px}
.read-more{position:absolute;right:26px;bottom:26px;font-size:13px;font-weight:600;display:flex;align-items:center;gap:10px;text-transform:uppercase}
.read-more b{width:22px;height:22px;border-radius:50%;background:var(--orange);display:inline-flex;align-items:center;justify-content:center}

/* about */
.about{position:absolute;top:1080px;left:0;width:1200px;height:560px}
.about-photo{position:absolute;left:120px;top:8px;width:352px;height:464px;background:linear-gradient(180deg,#a9b8c6 0%,#7f8c76 55%,#4d5846 100%)}
.stat{position:absolute;left:80px;top:408px;width:244px;height:112px;background:var(--orange);color:var(--white);padding:18px 28px}
.stat strong{font-size:52px;font-weight:700;line-height:1}
.stat span{display:block;font-size:12px;text-transform:uppercase;margin-top:4px;letter-spacing:.5px}
.about-copy{position:absolute;left:520px;top:20px;width:540px}
.about-copy h2{font-size:46px;font-weight:700;line-height:1.15}
.about-copy p{font-size:15px;color:var(--text);line-height:1.75;margin:40px 0 60px}

/* services */
.services{position:absolute;top:1660px;left:0;width:1200px;height:600px;background:var(--blush)}
.section-title{text-align:center;font-size:40px;font-weight:700;text-transform:uppercase}
.services .section-title{margin-top:80px}
.service-grid{position:absolute;left:112px;top:180px;width:980px;display:flex;justify-content:space-between}
.service{width:310px;height:392px;background:var(--white)}
.service .ph{height:208px}
.service .body{padding:26px 28px}
.service h3{font-size:20px;font-weight:600}
.service p{font-size:13px;color:var(--muted);line-height:1.6;margin:10px 0 22px}
.service .more{font-size:12px;font-weight:600;text-transform:uppercase;display:flex;align-items:center;gap:8px}
.ph-a{background:linear-gradient(160deg,#9aa4ad,#5b6169)}
.ph-b{background:linear-gradient(160deg,#c0c8cf,#7a6f62)}
.ph-c{background:linear-gradient(160deg,#8fb6dc,#b7a48f)}

/* testimonials */
.testimonials{position:absolute;top:2280px;left:0;width:1200px;height:480px}
.testimonials .city{position:absolute;right:0;top:0;width:620px;height:480px;background:linear-gradient(180deg,#8d96a3 0%,#55606c 60%,#2c323a 100%);clip-path:polygon(22% 0,100% 0,100% 100%,0 100%)}
.testimonials h2{position:absolute;left:100px;top:62px;font-size:40px;font-weight:700;text-transform:uppercase}
.quote{position:absolute;left:100px;top:140px;width:520px;height:310px;background:var(--white);box-shadow:0 14px 40px rgba(0,0,0,.12);padding:40px 40px;z-index:2}
.quote .who{display:flex;align-items:center;gap:18px}
.avatar{width:78px;height:78px;border-radius:50%;background:linear-gradient(160deg,#c9a58a,#6e4f3d)}
.who h4{font-size:22px;font-weight:600}
.who span{font-size:13px;color:var(--muted)}
.stars{margin-left:auto;display:flex;gap:3px;background:var(--white);box-shadow:0 4px 14px rgba(0,0,0,.1);padding:8px 10px}
.quote p{font-size:15px;color:var(--text);line-height:1.75;margin-top:34px}

/* projects */
.projects{position:absolute;top:2780px;left:0;width:1200px;height:684px;background:var(--blush)}
.projects .section-title{margin-top:82px}
.project-grid{position:absolute;left:120px;top:172px;width:980px;display:flex;justify-content:space-between}
.project{width:300px}
.project .ph{height:280px;position:relative}
.date{position:absolute;right:14px;bottom:14px;width:76px;height:76px;background:var(--orange);color:var(--white);font-size:15px;font-weight:600;text-align:center;display:flex;align-items:center;justify-content:center;line-height:1.25}
.project h3{font-size:30px;font-weight:700;margin-top:22px;text-transform:uppercase}
.project p{font-size:13px;color:var(--text);line-height:1.5;margin:4px 0 8px}
.project a{font-size:13px;color:var(--orange);font-weight:600}
.ph-d{background:linear-gradient(160deg,#b9c3cc,#4f4943)}
.ph-e{background:linear-gradient(180deg,#a7c3dd,#6c7a5e)}
.ph-f{background:linear-gradient(180deg,#9fc0e0,#3a4a5e)}

/* call to action */
.cta{position:absolute;top:3472px;left:0;width:1200px;height:148px;background:linear-gradient(90deg,#3c3b3a,#7d6f62)}
.cta-panel{position:absolute;right:0;top:0;width:740px;height:148px;background:var(--orange);clip-path:polygon(9% 0,100% 0,100% 100%,0 100%);display:flex;align-items:center;padding-left:132px;gap:70px;color:var(--white)}
.cta-panel small{display:block;font-size:13px;font-weight:600;text-transform:uppercase;letter-spacing:1px}
.cta-panel h2{font-size:36px;font-weight:700}
.btn-dark{background:var(--night);height:56px;padding:0 30px;font-size:13px;gap:10px}

/* footer */
.site-footer{position:absolute;top:3620px;left:0;width:1200px;height:524px;background:var(--night);color:#c9c9ce}
.start{position:absolute;left:60px;top:96px;width:400px;height:300px;background:var(--night-2);padding:36px 34px}
.start h3{color:var(--white);font-size:22px;font-weight:600}
.start h3::first-letter{color:var(--orange)}
.start p{font-size:14px;line-height:1.7;margin:18px 0 28px}
.signup{display:flex;height:50px;border:1px solid #3a3d44}
.signup span{flex:1;display:flex;align-items:center;padding-left:16px;font-size:13px;color:var(--muted)}
.signup b{width:86px;background:var(--orange);color:var(--white);font-size:14px;font-weight:500;display:flex;align-items:center;justify-content:center}
.links{position:absolute;left:520px;top:100px;display:flex;gap:58px}
.links h4{color:var(--white);font-size:22px;font-weight:600;margin-bottom:20px}
.links h4::first-letter{color:var(--orange)}
.links li{list-style:none;font-size:14px;margin-bottom:12px;display:flex;align-items:center;gap:10px}
.links li::before{content:"";width:6px;height:6px;border-radius:50%;border:1px solid var(--orange)}
.contacts{position:absolute;left:520px;top:300px;display:flex;gap:70px}
.contact{display:flex;gap:16px;align-items:center;font-size:14px;line-height:1.5}
.contact i{width:50px;height:50px;background:var(--orange);display:flex;align-items:center;justify-content:center;flex-shrink:0}
.footer-rule{position:absolute;left:520px;right:60px;top:270px;border-top:1px solid #2f3238}
</style>
</head>
<body>

<section class="hero" role="img" aria-label="New York City skyline seen from a rooftop at dusk"></section>

<header class="site-header">
  <a class="brand" href="#"><span>BREL</span><span>Roofing</span></a>
  <div class="topbar">
    <span><i class="dot"><svg width="11" height="11" viewBox="0 0 24 24"><path fill="#fff" d="M6.6 10.8a15 15 0 0 0 6.6 6.6l2.2-2.2a1 1 0 0 1 1-.25 11.4 11.4 0 0 0 3.6.57 1 1 0 0 1 1 1V20a1 1 0 0 1-1 1A17 17 0 0 1 3 4a1 1 0 0 1 1-1h3.5a1 1 0 0 1 1 1c0 1.25.2 2.45.57 3.57a1 1 0 0 1-.25 1z"/></svg></i>555-014-2290</span>
    <span><i class="dot"><svg width="11" height="11" viewBox="0 0 24 24"><path fill="#fff" d="M2 5h20v14H2zm2 2v.5l8 5 8-5V7z"/></svg></i>info@brelroofing.example</span>
    <div class="socials"><i></i><i></i><i></i></div>
  </div>
  <nav class="main-nav"><a href="#">Home</a><a href="#">About</a><a href="#">Services</a><a href="#">Projects</a><a href="#">Contact</a></nav>
  <a class="header-cta" href="#">REQUEST A QUOTE</a>
</header>

<div class="hero-copy">
  <h1>Professional<br>&amp; Affordable<br><em>Roofing Services</em></h1>
  <p>We are a trusted and reputable roofing company specializing in new construction flat roof installation and repair.</p>
  <a class="btn" href="#">Request a Quote</a>
</div>

<div class="features">
  <article class="feature">
    <div class="icon"><svg width="50" height="50" viewBox="0 0 50 50" fill="none" stroke="#f26522" stroke-width="2.5"><path d="M5 24 25 10l20 14"/><path d="M10 22v18h30V22"/><path d="M10 30h30M10 35h30"/></svg></div>
    <h3>Perfect Installs</h3>
    <p>Flat roofs built to spec for every new construction project.</p>
    <a class="read-more" href="#">Read More <b><svg width="10" height="10" viewBox="0 0 10 10"><path d="M2 5h6M5 2l3 3-3 3" stroke="#fff" stroke-width="1.5" fill="none"/></svg></b></a>
  </article>
  <article class="feature">
    <div class="icon"><svg width="50" height="50" viewBox="0 0 50 50" fill="none" stroke="#f26522" stroke-width="2.5"><path d="M6 34 18 14h26L32 34z"/><path d="M12 24h26M22 14l-10 20M32 14 22 34"/></svg></div>
    <h3>Reliable Upgrades</h3>
    <p>Modern materials that extend the life of your roof.</p>
    <a class="read-more" href="#">Read More <b><svg width="10" height="10" viewBox="0 0 10 10"><path d="M2 5h6M5 2l3 3-3 3" stroke="#fff" stroke-width="1.5" fill="none"/></svg></b></a>
  </article>
  <article class="feature">
    <div class="icon"><svg width="50" height="50" viewBox="0 0 50 50" fill="none" stroke="#f26522" stroke-width="2.5"><path d="M6 26 25 10l19 16"/><path d="M12 22v18h26V22"/><path d="M21 40V30h8v10"/></svg></div>
    <h3>Upkeep &amp; Repair</h3>
    <p>Thorough inspections and fast, lasting flat roof repairs.</p>
    <a class="read-more" href="#">Read More <b><svg width="10" height="10" viewBox="0 0 10 10"><path d="M2 5h6M5 2l3 3-3 3" stroke="#fff" stroke-width="1.5" fill="none"/></svg></b></a>
  </article>
</div>

<section class="about">
  <div class="about-photo" role="img" aria-label="Rooftop terrace overlooking a lake and mountains"></div>
  <div class="stat"><strong>200+</strong><span>Projects Completed</span></div>
  <div class="about-copy">
    <h2>We Provide<br>Quality Roofing<br>Services.</h2>
    <p>Our team of highly skilled and dedicated roofing professionals understands the unique challenges and requirements of new construction projects. We work closely with builders, contractors, and architects to design and install flat roofs that meet the specific needs of each project.</p>
    <a class="btn" href="#">Request a Quote</a>
  </div>
</section>

<section class="services">
  <h2 class="section-title">Our Services</h2>
  <div class="service-grid">
    <article class="service">
      <div class="ph ph-a" role="img" aria-label="Crew installing a flat roof membrane"></div>
      <div class="body"><h3>Flat Roof Installation</h3><p>New construction flat roofs designed and installed for lasting performance.</p><a class="more" href="#">Read More <svg width="14" height="14" viewBox="0 0 14 14"><circle cx="7" cy="7" r="7" fill="#1d1d1f"/><path d="M4 7h6M7.5 4.5 10 7l-2.5 2.5" stroke="#fff" stroke-width="1.4" fill="none"/></svg></a></div>
    </article>
    <article class="service">
      <div class="ph ph-b" role="img" aria-label="Roofer repairing a damaged roof"></div>
      <div class="body"><h3>Roof Repair</h3><p>We find the root cause and repair your flat roof with quality materials.</p><a class="more" href="#">Read More <svg width="14" height="14" viewBox="0 0 14 14"><circle cx="7" cy="7" r="7" fill="#1d1d1f"/><path d="M4 7h6M7.5 4.5 10 7l-2.5 2.5" stroke="#fff" stroke-width="1.4" fill="none"/></svg></a></div>
    </article>
    <article class="service">
      <div class="ph ph-c" role="img" aria-label="Roofer fixing storm damage on a rooftop"></div>
      <div class="body"><h3>Storm Damage</h3><p>Fast response to storm damage to protect your property and occupants.</p><a class="more" href="#">Read More <svg width="14" height="14" viewBox="0 0 14 14"><circle cx="7" cy="7" r="7" fill="#1d1d1f"/><path d="M4 7h6M7.5 4.5 10 7l-2.5 2.5" stroke="#fff" stroke-width="1.4" fill="none"/></svg></a></div>
    </article>
  </div>
</section>

<section class="testimonials">
  <div class="city" role="img" aria-label="City skyline with high-rise towers"></div>
  <h2>What Client Says</h2>
  <blockquote class="quote">
    <div class="who">
      <div class="avatar" role="img" aria-label="Client portrait"></div>
      <div><h4>Dana Whitfield</h4><span>CEO - Co Founder</span></div>
      <div class="stars">
        <svg width="80" height="14" viewBox="0 0 80 14"><g fill="#f26522"><path id="s" d="M7 0l2 4.6 5 .4-3.8 3.3 1.2 5L7 10.6 2.6 13.3l1.2-5L0 5l5-.4z"/><use href="#s" x="16"/><use href="#s" x="32"/><use href="#s" x="48"/><use href="#s" x="64"/></g></svg>
      </div>
    </div>
    <p>The team delivered our new flat roof on time and within budget. Their crew kept the site safe and tidy, and the finished roof has held up perfectly through every storm.</p>
  </blockquote>
</section>

<section class="projects">
  <h2 class="section-title">Our Recent Projects</h2>
  <div class="project-grid">
    <article class="project">
      <div class="ph ph-d" role="img" aria-label="Roofer torching a flat roof seam"><div class="date">APR 15<br>2023</div></div>
      <h3>Roof Repair</h3><p>Membrane seams resealed and drainage restored on a commercial flat roof.</p><a href="#">Read More</a>
    </article>
    <article class="project">
      <div class="ph ph-e" role="img" aria-label="Finished rooftop with city and hills behind"><div class="date">APR 15<br>2023</div></div>
      <h3>Roof Repair</h3><p>Leak traced and repaired on a residential complex rooftop terrace.</p><a href="#">Read More</a>
    </article>
    <article class="project">
      <div class="ph ph-f" role="img" aria-label="New flat roof on a residential building"><div class="date">APR 15<br>2023</div></div>
      <h3>Roof Repair</h3><p>Worn flashing replaced and surface coated to extend roof life.</p><a href="#">Read More</a>
    </article>
  </div>
</section>

<section class="cta">
  <div class="cta-panel">
    <div><small>Quality Roofing Provider</small><h2>Need roofing services?</h2></div>
    <a class="btn btn-dark" href="#"><svg width="14" height="14" viewBox="0 0 14 14"><circle cx="7" cy="7" r="7" fill="#fff"/><path d="M4 7h6M7.5 4.5 10 7l-2.5 2.5" stroke="#16181c" stroke-width="1.4" fill="none"/></svg>Discover More</a>
  </div>
</section>

<footer class="site-footer">
  <div class="start">
    <h3>Let's Get Started</h3>
    <p>Tell us about your flat roof project and our team will get back to you with a free estimate within one business day.</p>
    <div class="signup"><span>Email Address</span><b>Send</b></div>
  </div>
  <div class="links">
    <ul><h4>Explore</h4><li>About Us</li><li>Contact Us</li><li>Our Team</li></ul>
    <ul><h4>Services</h4><li>Roofing Layers</li><li>Roof Installation</li><li>Roof Renovation</li></ul>
    <ul><h4>Quicklinks</h4><li>Latest Articles</li><li>Privacy Policy</li><li>Refund &amp; Returns</li></ul>
  </div>
  <div class="footer-rule"></div>
  <div class="contacts">
    <div class="contact"><i><svg width="20" height="20" viewBox="0 0 24 24"><path fill="#fff" d="M6.6 10.8a15 15 0 0 0 6.6 6.6l2.2-2.2a1 1 0 0 1 1-.25 11.4 11.4 0 0 0 3.6.57 1 1 0 0 1 1 1V20a1 1 0 0 1-1 1A17 17 0 0 1 3 4a1 1 0 0 1 1-1h3.5a1 1 0 0 1 1 1c0 1.25.2 2.45.57 3.57a1 1 0 0 1-.25 1z"/></svg></i><span>Talk to an Experts: Toll Free<br>hello@brelroofing.example</span></div>
    <div class="contact"><i><svg width="20" height="20" viewBox="0 0 24 24"><path fill="#fff" d="M12 2a7 7 0 0 0-7 7c0 5 7 13 7 13s7-8 7-13a7 7 0 0 0-7-7zm0 9.5A2.5 2.5 0 1 1 12 6.5a2.5 2.5 0 0 1 0 5z"/></svg></i><span>27 Harbor Lane, Eastport,<br>United States of America</span></div>
  </div>
</footer>

</body>
</html>
```